Company Presentation re-design.

We need to create a new 15-20 pager-presentation that will show KORVALE (travel management company) as a client-centric company with a human-to-human approach. As a start we ask a Designers to create a 3 page test presentation so we can choose the winner. who will then design the rest slides

Two main idears are to be shown on the slides:
• KORVALE is client-centric company who believes in partnership with corporate clients;
• KORVALE is a stable and trustworthy partner;

The test slides should be:

Slide (1) - Our strategy is Customer – centric strategy. KORVALE bases its business approach on the customer needs. 5 qualities that identify KORVALE as a customer-centric :
1. corporate culture, aimed at customers' changing needs
2. professional Key Account Manager (KAM)
3. Each product solution meets specific client needs.
4. innovation
5. security policy

Slide (2) - Our product solutions of clients needs
The main idea of this page is to describe our products for customers. KORVALE has 5 main products:
1. Business Travel
2. Service
3. On-line booking
4. MICE & Congress
5. Non-standard services

Slide (3)
This page shows the highlights of KORVALE support and it is shown in a cloud design now.

Attched pls find our current presentation

Dear Professionals! Please pay attantion that we updated the project by doubled the budjet! Wait for yiour grate ideas. 

Target Market(s)

Mid to top management (practically any industry), travel coordinators, procurement specialists, corporate buyers etc, travelers

Industry/Entity Type

Security

Requirements
Must have
• (1) The presentation must visualize the text above, with as little text itself as possible.
(2) We would appreciate ideas with INFOGRAPHIC
(3) Design of the presentation is up to the company logo in all variations. ( attached files).
(4) We would like to see designs that use grey, blue, orange and maroon colors - corporate colors of our logo.
Nice to have
• Infografics
Designs we like:
to brintaly.com+; zumoth.com; pelvanstudio.com; tarnowatt.co.uk (infografics)

```html
<!DOCTYPE html>
<html lang="en">
<head>
<meta charset="utf-8">
<title>KORVALE – Customer Centric Strategy</title>
<link rel="stylesheet" href="https://fonts.googleapis.com/css2?family=Ubuntu:wght@300;400&display=swap">
<style>
  :root {
    --backdrop: #2b2b2b;
    --slide-light: #ffffff;
    --slide-edge: #dcdcdc;
    --brand-blue: #3d7cc4;
    --footer-blue: #3a78bf;
    --brand-grey: #7c7c7c;
    --brand-orange: #f0812f;
    --brand-red: #e1363b;
    --text-grey: #666666;
    --ring-grey: #cfcfcf;
    --logo-ink: #5d6a76;
    --white: #ffffff;
  }
  * { box-sizing: border-box; margin: 0; padding: 0; }
  html, body { width: 1200px; height: 695px; overflow: hidden; }
  body {
    background: var(--backdrop);
    font-family: "Ubuntu", Arial, sans-serif;
    position: relative;
  }
  .icon-defs { position: absolute; width: 0; height: 0; }

  .slide {
    position: absolute;
    width: 573px;
    height: 322px;
    overflow: hidden;
    background: radial-gradient(ellipse at 45% 50%, var(--slide-light) 25%, var(--slide-edge) 100%);
  }
  .slide--pictured { left: 20px; top: 17px; }
  .slide--outlined { left: 607px; top: 17px; }
  .slide--solid { left: 346px; top: 352px; }

  .slide__title {
    position: absolute;
    left: 14px;
    top: 16px;
    font-weight: 300;
    font-size: 23px;
    color: var(--brand-blue);
    z-index: 2;
  }
  .slide__brand {
    position: absolute;
    right: 16px;
    top: 9px;
    font-weight: 300;
    font-size: 19px;
    letter-spacing: 0.5px;
    color: var(--logo-ink);
    z-index: 2;
  }
  .slide__footer {
    position: absolute;
    left: 0; right: 0; bottom: 0;
    height: 14px;
    background: var(--footer-blue);
    color: var(--white);
    font-size: 8.5px;
    line-height: 14px;
    padding: 0 7px;
    display: flex;
    justify-content: space-between;
    z-index: 2;
  }

  .travellers-photo {
    position: absolute;
    left: 330px;
    top: 0;
    width: 243px;
    height: 308px;
    background: linear-gradient(90deg, rgba(235,235,235,0) 0%, #e2e3e4 35%, #c4c7ca 70%, #d6d8da 100%);
  }

  .pillars { position: absolute; display: flex; z-index: 1; }
  .pillar { display: flex; flex-direction: column; align-items: center; }
  .pillar__disc {
    width: 86px; height: 86px;
    border-radius: 50%;
    display: flex; align-items: center; justify-content: center;
  }
  .pillar__icon { width: 54px; height: 54px; }
  .pillar__label { font-size: 10px; line-height: 12px; }

  /* variant: white discs with grey ring */
  .slide--pictured .pillars { left: 16px; top: 111px; }
  .slide--pictured .pillar { width: 91px; }
  .slide--pictured .pillar__disc {
    width: 86px; height: 86px;
    background: var(--white);
    border: 3px solid var(--ring-grey);
    box-shadow: 0 1px 3px rgba(0,0,0,0.15);
  }
  .slide--pictured .pillar__label {
    margin-top: 26px;
    color: var(--brand-blue);
    text-align: left;
    width: 80px;
  }
  .pillar__brand-name {
    font-weight: 300;
    font-size: 16px;
    color: var(--logo-ink);
  }

  /* variant: dashed outline with label tags */
  .slide--outlined .pillars { left: 8px; top: 105px; }
  .slide--outlined .pillar { width: 110px; }
  .slide--outlined .pillar__disc { border: 1px dashed var(--tone); color: var(--tone); }
  .slide--outlined .pillar__label {
    margin-top: 7px;
    width: 86px;
    height: 29px;
    display: flex; align-items: center; justify-content: center;
    text-align: center;
    color: var(--white);
    background: var(--tone);
  }

  /* variant: solid discs */
  .slide--solid .pillars { left: 8px; top: 102px; }
  .slide--solid .pillar { width: 111px; }
  .slide--solid .pillar__disc { background: var(--tone); }
  .slide--solid .pillar__icon { color: var(--white); }
  .slide--solid .pillar__label {
    margin-top: 11px;
    color: var(--text-grey);
    text-align: center;
    width: 76px;
  }

  .tone-blue { --tone: var(--brand-blue); }
  .tone-grey { --tone: var(--brand-grey); }
  .tone-orange { --tone: var(--brand-orange); }
  .tone-red { --tone: var(--brand-red); }
  .slide--pictured .pillar__disc.tone-blue,
  .slide--pictured .pillar__disc.tone-grey,
  .slide--pictured .pillar__disc.tone-orange,
  .slide--pictured .pillar__disc.tone-red { color: var(--tone); }
</style>
</head>
<body>

<svg class="icon-defs" aria-hidden="true">
  <defs>
    <symbol id="icon-changing-needs" viewBox="0 0 100 100">
      <path d="M78 58 A32 32 0 1 1 66 22" fill="none" stroke="currentColor" stroke-width="12"/>
      <path d="M58 8 L88 20 L66 42 Z" fill="currentColor"/>
      <rect x="34" y="44" width="30" height="22" rx="3" fill="currentColor"/>
      <rect x="43" y="39" width="12" height="6" rx="2" fill="none" stroke="currentColor" stroke-width="3"/>
    </symbol>
    <symbol id="icon-account-manager" viewBox="0 0 100 100">
      <path d="M22 10 H12 V22 M78 10 H88 V22 M12 62 V74 H22 M88 62 V74 H78" fill="none" stroke="currentColor" stroke-width="4"/>
      <ellipse cx="50" cy="36" rx="15" ry="19" fill="currentColor"/>
      <path d="M14 96 Q16 66 40 62 L50 74 L60 62 Q84 66 86 96 Z" fill="currentColor"/>
    </symbol>
    <symbol id="icon-target" viewBox="0 0 100 100">
      <circle cx="46" cy="54" r="38" fill="none" stroke="currentColor" stroke-width="9"/>
      <circle cx="46" cy="54" r="22" fill="none" stroke="currentColor" stroke-width="8"/>
      <circle cx="46" cy="54" r="7" fill="currentColor"/>
      <path d="M46 54 L84 16" stroke="currentColor" stroke-width="5"/>
      <path d="M80 6 L82 18 L94 20 L86 28 L74 26 L72 14 Z" fill="currentColor"/>
    </symbol>
    <symbol id="icon-bulb" viewBox="0 0 100 100">
      <path d="M50 24 A22 22 0 0 1 64 63 V72 H36 V63 A22 22 0 0 1 50 24 Z" fill="none" stroke="currentColor" stroke-width="6"/>
      <rect x="38" y="76" width="24" height="5" fill="currentColor"/>
      <rect x="41" y="84" width="18" height="5" fill="currentColor"/>
      <path d="M50 4 V14 M22 14 L28 22 M78 14 L72 22 M8 40 H18 M82 40 H92 M14 66 L22 60 M86 66 L78 60" stroke="currentColor" stroke-width="5"/>
      <path d="M43 62 V50 L50 44 L57 50 V62" fill="none" stroke="currentColor" stroke-width="3"/>
    </symbol>
    <symbol id="icon-security" viewBox="0 0 100 100">
      <path d="M18 50 Q18 14 46 14 Q74 14 74 50 Z" fill="currentColor"/>
      <ellipse cx="46" cy="52" rx="16" ry="14" fill="currentColor"/>
      <path d="M8 96 Q10 70 34 66 L46 76 L58 66 Q70 68 74 74 V96 Z" fill="currentColor"/>
      <path d="M66 58 L80 52 L94 58 V74 Q94 88 80 94 Q66 88 66 74 Z" fill="currentColor" stroke="var(--white)" stroke-width="3"/>
    </symbol>
  </defs>
</svg>

<section class="slide slide--pictured">
  <h1 class="slide__title">Customer Centric Strategy</h1>
  <div class="travellers-photo" role="img" aria-label="Photograph of two business travellers walking through an airport terminal with wheeled luggage"></div>
  <div class="slide__brand">KORVALE</div>
  <div class="pillars">
    <div class="pillar"><div class="pillar__disc tone-blue"><svg class="pillar__icon"><use href="#icon-changing-needs"/></svg></div><p class="pillar__label">Meeting customers changing needs</p></div>
    <div class="pillar"><div class="pillar__disc tone-grey"><svg class="pillar__icon"><use href="#icon-account-manager"/></svg></div><p class="pillar__label">Professional Key Account Manager</p></div>
    <div class="pillar"><div class="pillar__disc tone-orange"><svg class="pillar__icon"><use href="#icon-target"/></svg></div><p class="pillar__label">Meeting specific client needs</p></div>
    <div class="pillar"><div class="pillar__disc tone-red"><svg class="pillar__icon"><use href="#icon-bulb"/></svg></div><p class="pillar__label">Innovative Approach</p></div>
    <div class="pillar"><div class="pillar__disc tone-blue"><svg class="pillar__icon"><use href="#icon-security"/></svg></div><p class="pillar__label">Novel security policy</p></div>
    <div class="pillar"><div class="pillar__disc"><span class="pillar__brand-name">KORVALE</span></div></div>
  </div>
  <footer class="slide__footer"><span>Always learning – always growing</span><span>Confidential © 2014</span></footer>
</section>

<section class="slide slide--outlined">
  <h1 class="slide__title">Customer Centric Strategy</h1>
  <div class="slide__brand">KORVALE</div>
  <div class="pillars">
    <div class="pillar tone-blue"><div class="pillar__disc"><svg class="pillar__icon"><use href="#icon-changing-needs"/></svg></div><p class="pillar__label">Meeting changing needs</p></div>
    <div class="pillar tone-grey"><div class="pillar__disc"><svg class="pillar__icon"><use href="#icon-account-manager"/></svg></div><p class="pillar__label">Professional Key Account Manager</p></div>
    <div class="pillar tone-orange"><div class="pillar__disc"><svg class="pillar__icon"><use href="#icon-target"/></svg></div><p class="pillar__label">Meeting specific client needs</p></div>
    <div class="pillar tone-red"><div class="pillar__disc"><svg class="pillar__icon"><use href="#icon-bulb"/></svg></div><p class="pillar__label">Innovative Approach</p></div>
    <div class="pillar tone-blue"><div class="pillar__disc"><svg class="pillar__icon"><use href="#icon-security"/></svg></div><p class="pillar__label">Novel security policy</p></div>
  </div>
  <footer class="slide__footer"><span>Always learning – always growing</span><span>Confidential © 2014</span></footer>
</section>

<section class="slide slide--solid">
  <h1 class="slide__title">Customer Centric Strategy</h1>
  <div class="slide__brand">KORVALE</div>
  <div class="pillars">
    <div class="pillar tone-blue"><div class="pillar__disc"><svg class="pillar__icon"><use href="#icon-changing-needs"/></svg></div><p class="pillar__label">Meeting customers changing needs</p></div>
    <div class="pillar tone-grey"><div class="pillar__disc"><svg class="pillar__icon"><use href="#icon-account-manager"/></svg></div><p class="pillar__label">Professional Key Account Manager</p></div>
    <div class="pillar tone-orange"><div class="pillar__disc"><svg class="pillar__icon"><use href="#icon-target"/></svg></div><p class="pillar__label">Meeting specific client needs</p></div>
    <div class="pillar tone-red"><div class="pillar__disc"><svg class="pillar__icon"><use href="#icon-bulb"/></svg></div><p class="pillar__label">Innovative Approach</p></div>
    <div class="pillar tone-blue"><div class="pillar__disc"><svg class="pillar__icon"><use href="#icon-security"/></svg></div><p class="pillar__label">Novel security policy</p></div>
  </div>
  <footer class="slide__footer"><span>Always learning – always growing</span><span>Confidential © 2014</span></footer>
</section>

</body>
</html>
```